Gymnastics Award Design Needed--for kids

Need a gymnastics certificate or award designed. Will be printed on a piece of 8.5x11 paper. The award will be celebrating the gymnast learning a new skill in gymnastics. So it should be fun, but still look "official". Needs to look good hanging on a gymnast's bedroom wall.

It should say "The Aerial Cartwheel Club"
I will be using this design to change it based on the skill.

My main colors are:
#34475D
#E1467A
#7555A4

So should use those, but can add others

My website is tumblenestpro.com so you can see the look/feel.

Target Market(s)

Main audience will be girls ages 5-12, but will also be used by slightly older girls and boys. So needs to be fun, not too gender specific.

Industry/Entity Type

Learning

Requirements
Must have
• The following will need to go on the certificate:
• * Name of Skill
• * Image of Skill
• * Gymnast's Name
• * my logo
• * Gym's Logo
• * Gym's Name
• Optional: Date

```html
<!DOCTYPE html>
<html lang="en">
<head>
<meta charset="utf-8">
<title>The Aerial Cartwheel Club Award</title>
<link rel="stylesheet" href="https://fonts.googleapis.com/css2?family=Montserrat:wght@400;500;700&family=Kaushan+Script&display=swap">
<style>
  :root {
    --pink: #E1467A;
    --purple: #7555A4;
    --ink: #333031;
    --frame-grey: #B3B3B3;
    --muted-grey: #A8A8A8;
    --paper: #FFFFFF;
    --page: #FFFFFF;
    --skin: #F1D3B0;
  }
  html, body {
    margin: 0;
    padding: 0;
    width: 1200px;
    height: 1200px;
    overflow: hidden;
    background: var(--page);
  }
  .canvas {
    position: relative;
    width: 1200px;
    height: 1200px;
    font-family: "Montserrat", sans-serif;
    color: var(--ink);
  }
  .backing {
    position: absolute;
    left: 0;
    top: 0;
  }
  .certificate {
    position: absolute;
    left: 176px;
    top: 284px;
    width: 850px;
    height: 632px;
    background: var(--paper);
  }
  .certificate__frame {
    position: absolute;
    left: 21px;
    top: 21px;
    width: 802px;
    height: 583px;
    border: 3px solid var(--frame-grey);
  }
  .club-name,
  .award-title,
  .presented-to,
  .presenter {
    position: absolute;
    left: 0;
    width: 850px;
    text-align: center;
    margin: 0;
  }
  .club-name {
    top: 51px;
    font-size: 22px;
    font-weight: 500;
    letter-spacing: 4px;
  }
  .award-title {
    top: 129px;
    font-size: 53px;
    font-weight: 700;
    letter-spacing: 2px;
  }
  .presented-to {
    top: 200px;
    font-size: 16px;
    font-weight: 500;
    letter-spacing: 1.5px;
  }
  .name-banner {
    position: absolute;
    left: 192px;
    top: 249px;
  }
  .gymnast-name {
    position: absolute;
    left: 192px;
    top: 249px;
    width: 464px;
    height: 69px;
    line-height: 69px;
    text-align: center;
    font-family: "Kaushan Script", cursive;
    font-size: 50px;
    color: var(--paper);
    margin: 0;
  }
  .presenter {
    top: 333px;
    font-size: 17px;
    font-weight: 500;
    line-height: 22px;
    letter-spacing: 1.5px;
  }
  .skill-illustration {
    position: absolute;
    left: 200px;
    top: 402px;
    width: 448px;
    height: 110px;
    background: linear-gradient(180deg, #FFFFFF 0%, #FBE3E8 45%, var(--skin) 100%);
    border-bottom: 3px solid var(--frame-grey);
  }
  .partner-logo-slot {
    position: absolute;
    left: 50px;
    top: 545px;
    width: 280px;
    text-align: center;
    white-space: nowrap;
    font-size: 22px;
    font-weight: 400;
    line-height: 25px;
    letter-spacing: 3px;
    color: var(--muted-grey);
    margin: 0;
  }
  .brand-mark {
    position: absolute;
    left: 520px;
    top: 553px;
    display: flex;
    align-items: center;
    gap: 12px;
  }
  .brand-mark__dot {
    width: 24px;
    height: 24px;
    border-radius: 50%;
    background: var(--purple);
  }
  .brand-mark__name {
    font-size: 24px;
    font-weight: 500;
    letter-spacing: 1px;
    color: var(--pink);
    white-space: nowrap;
  }
</style>
</head>
<body>
<div class="canvas">
  <svg class="backing" width="1200" height="1200" viewBox="0 0 1200 1200" aria-hidden="true">
    <rect x="118" y="228" width="964" height="744" fill="var(--pink)"/>
    <polygon points="996,228 1082,228 1082,972 700,590" fill="var(--purple)"/>
    <polygon points="368,916 1026,916 1082,972 320,972" fill="var(--page)"/>
  </svg>

  <section class="certificate">
    <div class="certificate__frame"></div>

    <p class="club-name">THE AERIAL CARTWHEEL CLUB</p>
    <h1 class="award-title">TITLE OF THE AWARD</h1>
    <p class="presented-to">is presented to</p>

    <svg class="name-banner" width="464" height="69" viewBox="0 0 464 69" aria-hidden="true">
      <polygon points="0,0 464,0 448,34.5 464,69 0,69 16,34.5" fill="var(--ink)"/>
    </svg>
    <p class="gymnast-name">Lily Carter</p>

    <p class="presenter">by Maple Ridge Gymnastic Gym on this<br>February 17, 2017</p>

    <div class="skill-illustration" role="img" aria-label="Illustration of a gymnast performing the aerial cartwheel in sequence"></div>

    <p class="partner-logo-slot">ANOTHER LOGO<br>GOES HERE</p>

    <div class="brand-mark">
      <span class="brand-mark__dot"></span>
      <span class="brand-mark__name">TUMBLENEST PRO</span>
    </div>
  </section>
</div>
</body>
</html>
```